Business card for medical clinic

I need an upmarket, modern medical/health business card for my clinic

Contact Information for Business Card

name, address, email, qr code

```html
<!DOCTYPE html>
<html lang="en">
<head>
<meta charset="utf-8">
<title>Meridian Care – Business Card</title>
<link href="https://fonts.googleapis.com/css2?family=Bodoni+Moda:wght@600&family=EB+Garamond:wght@400;700&display=swap" rel="stylesheet">
<style>
  :root{
    --page-bg:#c8f0fe;
    --card-bg:#eaf6fc;
    --glow:#8ee8ff;
    --navy:#1d5a8c;
    --ink:#2a3350;
    --accent:#29aee4;
    --stripe-pale:#cfe7f6;
    --stripe-mid:#7fcdf0;
    --stripe-bright:#00b4e6;
  }
  *{margin:0;padding:0;box-sizing:border-box}
  html,body{width:1137px;height:1200px;overflow:hidden}
  body{background:var(--page-bg);position:relative;font-family:"EB Garamond",serif}
  .card{position:absolute;width:807px;height:462px;background:var(--card-bg);box-shadow:0 10px 28px var(--glow);overflow:hidden}
  .card--front{left:164px;top:79px}
  .card--back{left:154px;top:647px;width:808px}

  .front-pattern{position:absolute;inset:0;
    background:linear-gradient(110deg,var(--card-bg) 0%,var(--stripe-pale) 30%,var(--stripe-mid) 62%,var(--stripe-bright) 88%);}

  .brand{position:absolute;font-family:"EB Garamond",serif;font-weight:400;color:var(--navy);white-space:nowrap;line-height:1}
  .card--front .brand{left:0;right:0;top:0;bottom:0;display:flex;align-items:center;justify-content:center;font-size:62px}
  .card--back .brand{left:44px;top:211px;width:360px;text-align:center;font-size:42px}

  .divider{position:absolute;left:428px;top:106px;width:2px;height:246px;background:var(--accent)}
  .person{position:absolute;left:473px;top:112px}
  .person__name{font-family:"Bodoni Moda",serif;font-weight:600;font-size:30px;color:var(--accent);line-height:1.1}
  .person__role{font-family:"EB Garamond",serif;font-weight:700;font-size:13px;color:var(--ink);margin-top:10px}
  .contacts{position:absolute;left:473px;top:179px;list-style:none}
  .contacts li{display:flex;align-items:center;height:45px;font-size:16.5px;color:var(--ink)}
  .contacts .icon{width:34px;height:34px;margin-right:18px;flex:none}
</style>
</head>
<body>
  <section class="card card--front">
    <div class="front-pattern" role="img" aria-label="Sweeping curved stripe pattern in pale to bright blue"></div>
    <div class="brand">Meridian Care</div>
  </section>

  <section class="card card--back">
    <div class="brand">Meridian Care</div>
    <div class="divider"></div>
    <div class="person">
      <h1 class="person__name">Daniel Harper</h1>
      <p class="person__role">CEO &amp; Founder</p>
    </div>
    <ul class="contacts">
      <li>
        <svg class="icon" viewBox="0 0 34 34" fill="none" stroke="#29aee4" stroke-width="1.3"><circle cx="17" cy="17" r="16"/><path d="M11 10.5l3-1 2 4-2 1.5a9 9 0 0 0 4.5 4.5l1.5-2 4 2-1 3c-6 1-13-6-12-12z" stroke-linejoin="round"/></svg>
        +1 (0) 555 014 272
      </li>
      <li>
        <svg class="icon" viewBox="0 0 34 34" fill="none" stroke="#29aee4" stroke-width="1.3"><circle cx="17" cy="17" r="16"/><rect x="10" y="12" width="14" height="10"/><path d="M10 12l7 5.5 7-5.5M10 22l5-4.5M24 22l-5-4.5"/></svg>
        your@email.com
      </li>
      <li>
        <svg class="icon" viewBox="0 0 34 34" fill="none" stroke="#29aee4" stroke-width="1.3"><circle cx="17" cy="17" r="16"/><path d="M17 25s-6-6.5-6-11a6 6 0 0 1 12 0c0 4.5-6 11-6 11z"/><circle cx="17" cy="14" r="2"/></svg>
        Building floor, NYC, USA
      </li>
      <li>
        <svg class="icon" viewBox="0 0 34 34" fill="none" stroke="#29aee4" stroke-width="1.3"><circle cx="17" cy="17" r="16"/><circle cx="17" cy="17" r="7.5"/><ellipse cx="17" cy="17" rx="3.2" ry="7.5"/><path d="M9.5 17h15M11 13h12M11 21h12"/></svg>
        www.meridiancareclinic.com
      </li>
    </ul>
  </section>
</body>
</html>
```